Brochure Design Project

CutiSure, PLLC PA is a full-service dermatopathology lab. To enable rapid turn around of your biopsy results, our facility offers:
• Routine processing,
• Special stains,
• Immunohistochemical stains and
• Direct immunofluorescence
In most cases results are available the next day.

We offer skin and mucosal biopsy interpretations for:
Rashes
Blisters
Bumps
Pigmented lesions
Hair loss

We provide pre-filled biopsy containers, specimen labels, shipping supplies and on-line ordering.
Results are available on a password-protected website.

The attached images are for ideas. You do not need to use all or any of them, except the logo, which needs to be used.

Just to clarify, this will be a trifold mail-out brochure.  One panel should have our contact information (return address) on the upper left and a place to write the recipients address.  This panel will be in landscape layout. 

Thank you.

I have seen some nice designs.  Was hoping to have more to choose from before making a final selection.  Keep it professional and bright and show me your creativity!

Target Market(s)

This brochure will be a marketing effort, the first since we've opened. The target audience is other physicians. Any physician who treats skin can benefit from our service, e.g. dermatologist, family doc, internal medicine, podiatrist, pediatrician, gynecologist, oral surgeon

Industry/Entity Type

Shipping

Requirements
Must have
• please use our logo (uploaded) and contact information:
CutiSure, PLLC, PA
4512 Tenbrook Ave, North Little Rock, AR 72118
501.486.2370
501.486.2375 Fax
www.CutiSurePLLC-example.com
Nice to have
• The other uploaded images can be used. There may be more, if I come across photogenic slides.
a short bio:
Dr. Vornell is a 1996 graduate of Pellham College School of Medicine. She received her pathology residency training at Pellham College Hospital and Corvath Valley Medical Systems and speciality training in dermatopathology at Ashgrove Bennet Hospital. She spent 10 years on the faculty at the Drummore Institute for Medical Sciences where she taught medical students, pathology residents, dermatology residents and directed the dermatopathology fellowship training program. She has published peer-reviewed original research, authored chapters and books and has lectured locally, nationally and internationally.
Should not have
• This is a laboratory.
I do not see patients or treat patients, only make diagnosis. Images that imply I am a clinic or offer patient care cause legal problems.

```html
<!DOCTYPE html>
<html lang="en">
<head>
<meta charset="utf-8">
<title>CutiSure Trifold Brochure – Outside</title>
<link rel="stylesheet" href="https://fonts.googleapis.com/css2?family=Lato:wght@400;700;900&family=Source+Sans+3:wght@300;400;600&display=swap">
<style>
  :root {
    --purple-top: #9c6ca8;
    --purple-bottom: #663b84;
    --navy: #0f4a86;
    --navy-deep: #0b3564;
    --rule: rgba(255,255,255,0.35);
    --ink-blue: #1c4f91;
    --web-purple: #6a3a8c;
    --grey-box: #e7e8ea;
    --grey-text: #a8abb0;
    --stamp-line: #2e5a96;
    --white: #ffffff;
  }
  * { margin: 0; padding: 0; box-sizing: border-box; }
  html, body { width: 1200px; height: 848px; overflow: hidden; background: var(--white); }
  .brochure { position: relative; width: 1200px; height: 848px; overflow: hidden; font-family: "Source Sans 3", sans-serif; }

  /* Left panel */
  .panel-services {
    position: absolute; left: 0; top: 0; width: 404px; height: 848px;
    background: linear-gradient(180deg, var(--purple-top), var(--purple-bottom));
    color: var(--white); padding: 56px 20px 0 50px;
  }
  .services-title { font-family: "Lato", sans-serif; font-weight: 700; font-size: 17.5px; line-height: 22.5px; }
  .services-list { list-style: none; font-family: "Lato", sans-serif; font-weight: 700; font-size: 17.5px; line-height: 22.8px; }
  .services-list li::before { content: "• "; }
  .divider { border: 0; border-top: 1px solid var(--rule); width: 308px; }
  .divider-top { margin-top: 24px; }
  .tagline { font-family: "Lato", sans-serif; font-weight: 700; font-size: 19.5px; line-height: 30px; padding: 11px 0 13px; }
  .about-title { font-family: "Lato", sans-serif; font-weight: 700; font-size: 23px; margin-top: 58px; letter-spacing: 0.3px; }
  .about-text { font-weight: 300; font-size: 16.6px; line-height: 22.5px; margin-top: 16px; width: 320px; }
  .about-text + .about-text { margin-top: 10px; }

  /* Middle panel */
  .panel-pathologist { position: absolute; left: 404px; top: 0; width: 403px; height: 848px; }
  .pathologist-art { position: absolute; left: 0; top: 0; }
  .pathologist-copy { position: absolute; left: 65px; top: 520px; width: 285px; color: var(--white); }
  .pathologist-title { font-family: "Lato", sans-serif; font-weight: 700; font-size: 23.5px; letter-spacing: 0.3px; }
  .pathologist-bio { font-weight: 300; font-size: 12.4px; line-height: 15.4px; margin-top: 10px; }
  .pathologist-bio + .pathologist-bio { margin-top: 15px; }

  /* Right (mailing) panel */
  .panel-mailer { position: absolute; left: 807px; top: 0; width: 393px; height: 848px; border-left: 1px solid #c9d3e0; }
  .stamp-box { position: absolute; left: 41px; top: 40px; width: 100px; height: 87px; border: 1px solid var(--stamp-line); }
  .stamp-line { position: absolute; left: 141px; right: 0; height: 8px; background: var(--stamp-line); }
  .stamp-line-1 { top: 74px; }
  .stamp-line-2 { top: 90px; height: 9px; }
  .address-box {
    position: absolute; left: 125px; top: 231px; width: 129px; height: 411px;
    background: var(--grey-box); border-radius: 6px;
    display: flex; align-items: center; justify-content: center;
  }
  .address-label { writing-mode: vertical-rl; transform: rotate(180deg); color: var(--grey-text); font-weight: 300; font-size: 18px; letter-spacing: 0.3px; }
  .brand-mark {
    position: absolute; left: 50px; top: 680px;
    writing-mode: vertical-rl; transform: rotate(180deg);
    display: flex; align-items: center; gap: 8px;
    font-family: "Lato", sans-serif; font-weight: 900; font-size: 26px; color: var(--ink-blue);
  }
  .brand-dot { width: 14px; height: 14px; border-radius: 50%; background: var(--ink-blue); }
  .return-address {
    position: absolute; left: 309px; bottom: 40px;
    writing-mode: vertical-rl; transform: rotate(180deg);
    color: var(--ink-blue); white-space: nowrap;
  }
  .return-name { font-family: "Lato", sans-serif; font-weight: 700; font-size: 16.5px; line-height: 19px; }
  .return-line { font-weight: 400; font-size: 14.2px; line-height: 19px; }
  .return-line .gap { display: inline-block; height: 18px; }
  .return-web { font-family: "Lato", sans-serif; font-weight: 700; font-size: 16px; line-height: 24px; color: var(--web-purple); }
</style>
</head>
<body>
<div class="brochure">

  <section class="panel-services">
    <p class="services-title">Offering skin, mucosal, hair and nail biopsy interpretations for:</p>
    <ul class="services-list">
      <li>Rashes</li>
      <li>Blisters</li>
      <li>Bumps</li>
      <li>Pigmented lesions</li>
      <li>Hair loss</li>
      <li>Nail disease</li>
    </ul>
    <hr class="divider divider-top">
    <p class="tagline">Our biopsy interpretation will<br>help your treatment plan.<br>It's the logical solution.</p>
    <hr class="divider">
    <h2 class="about-title">ABOUT US</h2>
    <p class="about-text">CutiSure, PLLC, PA is a dermatopathology laboratory located in central Arkansas,<br>owned by Lena R. Vornell, MD.</p>
    <p class="about-text">Dr. Vornell is board certified in Anatomical and Clinical Pathology and in Dermatopathology.</p>
    <p class="about-text">Dr. Vornell and her staff are dedicated to helping you care for your patients efficiently and effectively.</p>
    <p class="about-text">Dr. Vornell is available to discuss the best biopsy options for your patient as well as the results from that biopsy</p>
  </section>

  <section class="panel-pathologist">
    <svg class="pathologist-art" width="403" height="848" viewBox="0 0 403 848">
      <defs>
        <linearGradient id="portraitTone" x1="0" y1="0" x2="0.6" y2="1">
          <stop offset="0" stop-color="#e2cfa8"/>
          <stop offset="0.55" stop-color="#d9b79d"/>
          <stop offset="1" stop-color="#3a3330"/>
        </linearGradient>
        <linearGradient id="panelBlue" x1="0" y1="0" x2="0" y2="1">
          <stop offset="0" stop-color="#11538f"/>
          <stop offset="1" stop-color="#0b3564"/>
        </linearGradient>
      </defs>
      <path role="img" aria-label="Portrait photograph of the pathologist"
            d="M40,494 C60,300 90,60 210,30 C330,20 385,120 403,190 L403,494 Z"
            fill="url(#portraitTone)"/>
      <path d="M0,494 C190,470 350,360 403,185 L403,848 L0,848 Z" fill="url(#panelBlue)"/>
    </svg>
    <div class="pathologist-copy">
      <h2 class="pathologist-title">OUR PATHOLOGIST</h2>
      <p class="pathologist-bio">Dr. Vornell is a 1996 graduate of Pellham College School of Medicine. She received her pathology residency training at Pellham College Hospital and Corvath Valley Medical Systems and speciality training in dermatopathology at Ashgrove Bennet Hospital.</p>
      <p class="pathologist-bio">Dr. Vornell spent 10 years on the faculty at the Drummore Institute for Medical Sciences where she taught medical students, pathology residents, dermatology residents and directed the dermatopathology fellowship training program. She has published peer-reviewed original research, authored chapters and books and has lectured locally, nationally and internationally.</p>
    </div>
  </section>

  <section class="panel-mailer">
    <div class="stamp-box"></div>
    <div class="stamp-line stamp-line-1"></div>
    <div class="stamp-line stamp-line-2"></div>
    <div class="address-box"><span class="address-label">Client Address</span></div>
    <div class="brand-mark"><span class="brand-dot"></span><span>CutiSure</span></div>
    <address class="return-address" style="font-style:normal">
      <div class="return-name">CutiSure, PLLC, PA</div>
      <div class="return-line">4512 Tenbrook Ave, North Little Rock, AR 72118<span class="gap"></span>Tel : 501.486.2370<span class="gap"></span>Fax : 501.486.2375</div>
      <div class="return-web">www.CutiSurePLLC-example.com</div>
    </address>
  </section>

</div>
</body>
</html>
```